Fun footwear company needs a media card!

We are a fun footwear company called 'Puddle Pops' we are looking for a small media card to be sent out with our products.
The media card will showcase or newest product 'Puddle Ponchos' - it needs to include a small caption reading
'Hello, adventurer. It’s time to stomp around in the rain.Tag your travels @gosplashwild #ppops or visit us at facebook.com/gosplashwild'
We would like to include or logo (attached)
Also have something similar to the previous media card (attached)
I have attached an image of the product (please feel free to not include this is you think it does not work)
As we are a fun brand, all of our promotional media needs to be bright and fit in with our brand.
Visit our website to see our products www.pudpops.com.au

```html
<!DOCTYPE html>
<html lang="en">
<head>
<meta charset="utf-8">
<title>Puddle Pops – Media Card</title>
<link rel="stylesheet" href="https://fonts.googleapis.com/css2?family=Open+Sans:ital,wght@0,400;0,700;0,800;1,700;1,800&display=swap">
<style>
  :root {
    --pop-red: #e4232f;
    --sky-blue: #2fa3da;
    --paper: #ffffff;
    --ink: #111111;
    --trim: #b5b5b5;
    --mist: #eef5fa;
  }
  * { margin: 0; padding: 0; box-sizing: border-box; }
  html, body { width: 1187px; height: 1200px; overflow: hidden; background: var(--paper); }
  body { position: relative; font-family: "Open Sans", Arial, sans-serif; }

  .crop-marks { position: absolute; inset: 0; width: 1187px; height: 1200px; }
  .crop-marks line { stroke: var(--trim); stroke-width: 1; }

  /* Front panel */
  .card-front { position: absolute; left: 59px; top: 58px; width: 490px; height: 1084px; overflow: hidden; }
  .card-front svg { position: absolute; inset: 0; }
  .brand-name {
    position: absolute; left: 50%; top: 50%;
    font-weight: 800; white-space: nowrap; line-height: 1;
    transform: translate(-50%, -50%) rotate(90deg);
  }
  .card-front .brand-name { left: 43%; font-size: 148px; letter-spacing: -2px; color: var(--paper); }

  /* Back panel */
  .card-back { position: absolute; left: 642px; top: 58px; width: 486px; height: 1084px; }
  .greeting {
    position: absolute; left: 0; right: 0; top: 14px; text-align: center;
    font-style: italic; font-weight: 800; font-size: 104px; letter-spacing: -3px;
    color: var(--pop-red); line-height: 1;
  }
  .sky {
    position: absolute; left: 0; top: 140px; width: 486px; height: 844px;
    background: linear-gradient(to bottom, var(--sky-blue) 0%, var(--sky-blue) 42%, #9fd2ee 70%, var(--mist) 88%, var(--paper) 100%);
    overflow: hidden;
  }
  .sky-notch { position: absolute; left: 0; top: 0; }
  .greeting-sub {
    position: absolute; left: 0; right: 0; top: 4px; text-align: center;
    font-style: italic; font-weight: 800; font-size: 48px; color: var(--ink); letter-spacing: -1px;
  }
  .tagline {
    position: absolute; left: 0; right: 0; top: 122px; text-align: center;
    font-style: italic; font-weight: 700; font-size: 41px; line-height: 1.2; color: var(--paper);
  }
  .product-photo {
    position: absolute; left: 70px; top: 240px; width: 226px; height: 590px; border-radius: 40px;
    background: linear-gradient(to bottom, #e8d8cc 0%, #f4f7fa 35%, #3f4c6b 62%, #d9b49a 75%, #a9c4e6 100%);
    opacity: 0.85;
  }
  .card-back .brand-name {
    left: 350px; top: 554px; font-size: 64px; letter-spacing: -1px; color: var(--pop-red);
  }
  .social-strip {
    position: absolute; left: 0; top: 984px; width: 486px; height: 100px;
    background: var(--pop-red); color: var(--paper);
    display: flex; flex-direction: column; justify-content: center; align-items: center;
    font-size: 20px; line-height: 1.5;
  }
  .social-strip strong { font-weight: 700; }
</style>
</head>
<body>
  <svg class="crop-marks" viewBox="0 0 1187 1200" aria-hidden="true">
    <line x1="40" y1="0" x2="40" y2="40"/><line x1="0" y1="40" x2="40" y2="40"/>
    <line x1="568" y1="0" x2="568" y2="40"/><line x1="622" y1="0" x2="622" y2="40"/>
    <line x1="1147" y1="0" x2="1147" y2="40"/><line x1="1147" y1="40" x2="1187" y2="40"/>
    <line x1="40" y1="1160" x2="40" y2="1200"/><line x1="0" y1="1160" x2="40" y2="1160"/>
    <line x1="568" y1="1160" x2="568" y2="1200"/><line x1="622" y1="1160" x2="622" y2="1200"/>
    <line x1="1147" y1="1160" x2="1147" y2="1200"/><line x1="1147" y1="1160" x2="1187" y2="1160"/>
  </svg>

  <section class="card-front">
    <svg width="490" height="1084" viewBox="0 0 490 1084" aria-hidden="true">
      <rect width="490" height="1084" fill="var(--sky-blue)"/>
      <path d="M0 0H490V590C420 520 340 470 250 480C160 490 90 560 0 545Z" fill="var(--pop-red)"/>
    </svg>
    <div class="brand-name">Puddle Pops</div>
  </section>

  <section class="card-back">
    <h1 class="greeting">Hello,</h1>
    <div class="sky">
      <svg class="sky-notch" width="486" height="140" viewBox="0 0 486 140" aria-hidden="true">
        <path d="M60 0C80 120 410 120 430 0Z" fill="var(--paper)"/>
      </svg>
      <p class="greeting-sub">adventurer.</p>
      <p class="tagline">It’s time to stomp<br>around in the rain</p>
      <div class="product-photo" role="img" aria-label="Smiling model wearing a clear Puddle Ponchos rain jacket with blue trim, striped shorts and jelly sandals"></div>
      <div class="brand-name">Puddle Pops</div>
    </div>
    <footer class="social-strip">
      <span>Tag your travels <strong>@gosplashwild #ppops</strong></span>
      <span>or visit us at <strong>facebook.com/gosplashwild</strong></span>
    </footer>
  </section>
</body>
</html>
```